Impack Proof Screen Protector Packaging Design Project

I want a sleek box design for an Impact Proof Screen Protection Shield" for mobile phones and tablet screens. Want to use this design for online website sale (eCommerce). Please use the colour combination which can effect customers physiology immediately.
Product Features:
Name: vela Guardwrap
Advanced Impact Protection Shield
Easy and Fast Application
Compatible With Stylus
Guaranteed Glue Free
Perfect Crystal Clear
Anti Fingerprint
No Air Bubble
Anti Bacterial
Anti scratch
Updates

come on guys...give me some best designs please

Project Deadline Extended
Reason: Have not received the best design yet...

Project Deadline Extended
Reason: still waiting for the best design

Project Deadline Extended

Project Deadline Extended

Project Deadline Extended

Hi,

Thanks for the design. I would like to make some changes.

I want main core colour black (HTML code of Black is 111C24)
Blue colour as aditional or second colour, (HTML code of BLUE is 0088CE)

AND another colour like Orange (HTML -> FF5800)  or Purple (HTML -> 9B1889) can be use as a ACCENT colour if needed.

Pure White, Silver and Greys like -> HTML codes -> 4D4F53 , D1D4D3 , AND C4D9E4 Can be use as support colours if needed.

please work on it and get back to me .

Thanks

Project Deadline Extended
Reason: work pending

Target Market(s)

UK & Europe is priority and then Global market

Industry/Entity Type

Online

Requirements
Must have
• All features must write with Pictures/thumbnail on back side.
Must have a hanger hook / hole.
Must have Recycling sign/logo on the edge.
Must have our website name "vela.co" on somewhere
its a sleek box design, size - This packing will be in 2 sizes:
a). 27cm X 11cm X 2cm
b). 25cm X 20cm X 2cm
Nice to have
• Impact Protection is main feature in this product, so can be highlighted with some weapon like sword or something like this...
Should not have
• Please try to not use a picture of any device like kelphone etc. because this packing will be use for number of different king of mobile phone/tablet devices.

```html
<!DOCTYPE html>
<html lang="en">
<head>
<meta charset="utf-8">
<title>vela Guardwrap – Packaging Front</title>
<link rel="stylesheet" href="https://fonts.googleapis.com/css2?family=Roboto+Condensed:wght@700&family=Open+Sans:wght@300;700&display=swap">
<style>
  :root {
    --page-bg: #f2f3f4;
    --box-black: #111c24;
    --box-deep: #05080b;
    --blue: #0088ce;
    --blue-light: #3fc3f2;
    --orange: #ff8a00;
    --orange-deep: #ff5800;
    --silver: #d1d4d3;
    --grey: #4d4f53;
    --white: #ffffff;
  }
  * { box-sizing: border-box; margin: 0; padding: 0; }
  html, body { width: 1200px; height: 900px; overflow: hidden; }
  body { background: var(--page-bg); position: relative; font-family: "Open Sans", sans-serif; }

  .package { position: absolute; left: 210px; top: 40px; width: 780px; height: 830px; }

  .hanger-tab {
    position: absolute; left: 30px; top: 0; width: 680px; height: 170px;
    border-radius: 14px 14px 0 0; overflow: hidden;
    background: linear-gradient(160deg, var(--box-black) 0%, #1f3a4d 45%, var(--box-deep) 100%);
  }
  .hanger-hole {
    position: absolute; left: 50%; top: 40px; width: 150px; height: 34px;
    transform: translateX(-50%); border-radius: 17px; background: var(--page-bg);
  }

  .front-panel {
    position: absolute; left: 0; top: 170px; width: 720px; height: 660px;
    overflow: hidden;
    background: var(--box-black);
  }
  .background-art {
    position: absolute; inset: 0;
    background:
      radial-gradient(ellipse at 22% 30%, rgba(0,136,206,0.55) 0%, rgba(0,136,206,0) 45%),
      linear-gradient(135deg, #2a3238 0%, var(--box-black) 50%, var(--box-deep) 100%);
  }
  .side-panel {
    position: absolute; left: 720px; top: 170px; width: 60px; height: 660px;
    background: linear-gradient(90deg, #0b1116, #1c252c);
  }
  .side-url {
    position: absolute; left: 50%; top: 260px; transform: translateX(-50%) rotate(-90deg);
    color: var(--white); font-size: 26px; letter-spacing: 2px; white-space: nowrap;
  }

  .brand-word {
    position: absolute; right: 50px; top: 18px;
    font-family: "Roboto Condensed", sans-serif; font-weight: 700;
    font-size: 150px; line-height: 1; color: var(--orange); letter-spacing: 2px;
  }
  .product-name {
    position: absolute; right: 50px; top: 178px;
    font-family: "Roboto Condensed", sans-serif; font-weight: 700;
    font-size: 56px; line-height: 1.1; color: var(--white);
  }
  .tagline {
    position: absolute; right: 50px; top: 252px;
    font-weight: 300; font-size: 29px; line-height: 1.2; color: var(--white); white-space: nowrap;
  }

  .feature-grid {
    position: absolute; left: 55px; top: 400px;
    display: grid; grid-template-columns: repeat(3, 92px); gap: 14px;
  }
  .feature-tile {
    width: 92px; height: 104px; border-radius: 10px; padding: 8px 4px 8px;
    background: linear-gradient(180deg, var(--blue-light), var(--blue) 60%, #005a8a);
    border: 3px solid var(--grey);
    display: flex; flex-direction: column; align-items: center; justify-content: space-between;
  }
  .feature-icon {
    width: 44px; height: 44px; border-radius: 8px;
    background: rgba(255,255,255,0.28);
  }
  .feature-label {
    color: var(--white); font-weight: 700; font-size: 10px; line-height: 1.15; text-align: center;
  }

  .shield-art {
    position: absolute; left: 405px; top: 380px; width: 215px; height: 245px;
    border-radius: 18px;
    background: linear-gradient(180deg, #ffc04a 0%, var(--orange) 55%, var(--orange-deep) 100%);
  }
  .recycle-sign {
    position: absolute; left: 625px; top: 560px; width: 56px; height: 56px;
    border-radius: 50%; background: var(--orange);
  }
</style>
</head>
<body>
  <div class="package">
    <div class="hanger-tab" role="img" aria-label="Dark background with flowing blue and grey swooshes">
      <div class="hanger-hole"></div>
    </div>

    <div class="front-panel">
      <div class="background-art" role="img" aria-label="Dark background with flowing blue and grey swooshes"></div>

      <div class="brand-word">vela</div>
      <div class="product-name">Guardwrap</div>
      <div class="tagline">Advanced Impact Protection Shield</div>

      <div class="feature-grid">
        <div class="feature-tile"><span class="feature-icon" role="img" aria-label="Pictogram of a hand applying the film"></span><span class="feature-label">Easy and Fast Application</span></div>
        <div class="feature-tile"><span class="feature-icon" role="img" aria-label="Pictogram of crossed-out glue"></span><span class="feature-label">Guaranteed Glue Free</span></div>
        <div class="feature-tile"><span class="feature-icon" role="img" aria-label="Pictogram of a sparkle"></span><span class="feature-label">Perfect Crystal Clear</span></div>
        <div class="feature-tile"><span class="feature-icon" role="img" aria-label="Pictogram of crossed-out fingerprint"></span><span class="feature-label">Anti-Fingerprint</span></div>
        <div class="feature-tile"><span class="feature-icon" role="img" aria-label="Pictogram of crossed-out germ"></span><span class="feature-label">Anti-Bacterial</span></div>
        <div class="feature-tile"><span class="feature-icon" role="img" aria-label="Pictogram of crossed-out scratch"></span><span class="feature-label">Anti-Scratch</span></div>
      </div>

      <div class="shield-art" role="img" aria-label="Orange protection shield illustration with a silver tick"></div>
      <div class="recycle-sign" role="img" aria-label="Recycling sign"></div>
    </div>

    <div class="side-panel">
      <div class="side-url">vela.co</div>
    </div>
  </div>
</body>
</html>
```